Brightleaf Plots needs a business card

I need a business card using the logo that was selected. I would like the front to have the words "local", "sustainable", "healthy", and "elegant". I would also like the front to have my name on the card as Marisa Holcombe.

The back of the card can list what I do: Container Design & Installation, Vegetable Garden Design & Installation.
It can also list my contact information: Mobile Phone 914-583-6021, and email brightleafplots27@mailtrove.net

```html
<!DOCTYPE html>
<html lang="en">
<head>
<meta charset="utf-8">
<title>Brightleaf Plots – Business Card</title>
<link rel="stylesheet" href="https://fonts.googleapis.com/css2?family=Didact+Gothic&display=swap">
<style>
  :root {
    --page-bg: #ecebe8;
    --frame-green: #00a651;
    --card-white: #ffffff;
    --ink-navy: #2e3192;
    --ink-dark: #231f20;
    --mark-grey: #939598;
  }
  * { box-sizing: border-box; margin: 0; padding: 0; }
  html, body {
    width: 1200px;
    height: 686px;
    overflow: hidden;
    background: var(--page-bg);
    font-family: "Didact Gothic", "Helvetica Neue", Arial, sans-serif;
  }
  .canvas {
    position: relative;
    width: 1200px;
    height: 686px;
  }
  .card {
    position: absolute;
    top: 183px;
    width: 540px;
    height: 320px;
    background: var(--card-white);
    border: 22px solid var(--frame-green);
  }
  .card--front { left: 40px; }
  .card--back { left: 620px; }

  .brand-mark {
    position: absolute;
    width: 118px;
    height: 118px;
    border-radius: 50%;
    background: var(--mark-grey);
  }
  .brand-name {
    position: absolute;
    color: var(--ink-navy);
    white-space: nowrap;
  }

  /* Front */
  .card--front .brand-mark { left: 60px; top: 38px; }
  .card--front .brand-name { left: 119px; top: 170px; transform: translateX(-50%); font-size: 15px; }
  .holder-name {
    position: absolute; left: 218px; top: 50px;
    font-size: 27px; color: var(--ink-navy); white-space: nowrap;
  }
  .holder-role {
    position: absolute; left: 280px; top: 92px;
    font-size: 15px; color: var(--ink-navy);
  }
  .contact-list {
    position: absolute; left: 240px; top: 142px;
    list-style: none; font-size: 15px; line-height: 27px;
    color: var(--ink-navy); white-space: nowrap;
  }
  .tagline {
    position: absolute; left: 0; right: 0; top: 222px;
    text-align: center; font-size: 15.5px; color: var(--ink-dark);
  }

  /* Back */
  .card--back .brand-mark { left: 189px; top: 28px; }
  .card--back .brand-name { left: 0; right: 0; top: 158px; text-align: center; font-size: 19px; }
  .service-list {
    position: absolute; left: 0; right: 0; top: 198px;
    list-style: none; text-align: center;
    font-size: 15.5px; line-height: 20px; color: var(--ink-dark);
  }
</style>
</head>
<body>
<main class="canvas">
  <section class="card card--front" aria-label="Card front">
    <span class="brand-mark" aria-hidden="true"></span>
    <p class="brand-name">Brightleaf Plots</p>
    <h1 class="holder-name">Marisa Holcombe</h1>
    <p class="holder-role">Owner</p>
    <ul class="contact-list">
      <li>Mob : 914-583-6021</li>
      <li>Email : brightleafplots27@mailtrove.net</li>
    </ul>
    <p class="tagline">“Local, Sustainable, Healthy, &amp; Elegant”</p>
  </section>

  <section class="card card--back" aria-label="Card back">
    <span class="brand-mark" aria-hidden="true"></span>
    <p class="brand-name">Brightleaf Plots</p>
    <ul class="service-list">
      <li>Container Design &amp; Installation</li>
      <li>Vegetable Garden Design &amp; Installation</li>
    </ul>
  </section>
</main>
</body>
</html>
```